Players Card Designs - For Casino Group

We need a players card design for our casino group.
We need three types of players card designs. There are
1. Gold (Normal)
2. Platinum (Grander)
3. Vireo Card Limited ( Grandest)
Double Sided. Card dimensions are same as Credit Card.
Note: The card used is Smart Cards with sim-card type chip visible on the front.
So, please keep that in mind while designing.
Front Side:
Casino Group Logo (on All designs). Torvel Global is group logo.
Casino Logo
Card Type name (gold or platinum or Vireo Card Limited)
"Valid in all TORVEL GLOBAL Casinos" at the bottom.
Some insert this side arrow, or text...
IMPORTANT: At the bottom of the card, we will be embossing customer name and his ID. in one line
Example:
OWEN MARLOW ID: 123456
Back side:
Terms and Conditions in Two languages. English and Nederlands
Casino Address with phone number
www.torvelglobal.example
NO MAGNETIC STRIP. So, please use all the space.
Terms and Conditions:
In English:
This card is property of Torvel Global
This card is not transferable and may not be used by any person other than the named card holder
Lost, stolen or damaged cards are to be notified immediately to any Torvel Global Casino
Membership privileges are available only on the presentation of your current membership card together with photographic identification and proof of entitlement to any concession benefits
Management reserve the right to update or change the terms and conditions without prior notice and management decision is final
Use of this card constitutes acceptance of the terms and conditions
In Nederlandse:
Will be given Later
Note:
Use creative background and fonts..
Torvel Global is Group name. Logo is attached.
Mirabel Casino is one of the casino under torvelglobal. Logo attached.
We will need same design for other casinos as well. Only the logo and addresses will change. Those logos will be shared once the design is selected
Players Card Design. Double Sided.

```html
<!DOCTYPE html>
<html lang="en">
<head>
<meta charset="utf-8">
<title>Players Card Designs – Torvel Global</title>
<link href="https://fonts.googleapis.com/css2?family=Cinzel:wght@400;600;700&family=Open+Sans:wght@400;600&display=swap" rel="stylesheet">
<style>
  :root{
    --bg-light:#9aa0a2;
    --bg-dark:#4d5456;
    --black-1:#2a2a2a;
    --black-2:#0d0d0d;
    --gold-1:#f6e39a;
    --gold-2:#d4a73c;
    --gold-3:#a87a1c;
    --gold-text:#e2b548;
    --silver-1:#eef0f1;
    --silver-2:#b9bec1;
    --silver-3:#8e9498;
    --navy:#1d2d5a;
    --ink:#111;
    --white:#fff;
  }
  *{box-sizing:border-box;margin:0;padding:0}
  html,body{width:800px;height:1200px;overflow:hidden}
  body{
    background:radial-gradient(ellipse at 50% 45%, var(--bg-light) 0%, #7c8386 55%, var(--bg-dark) 100%);
    font-family:"Open Sans", Arial, sans-serif;
    position:relative;
  }
  .card{
    position:absolute;width:376px;height:240px;border-radius:8px;overflow:hidden;
    box-shadow:2px 4px 8px rgba(0,0,0,.45);
  }
  .front{left:12px}
  .back{left:413px}
  .row-1{top:160px}
  .row-2{top:487px}
  .row-3{top:800px}

  /* finishes */
  .finish-black{background:linear-gradient(180deg,#3a3a3a 0%,var(--black-1) 40%,var(--black-2) 100%)}
  .finish-silver{background:repeating-linear-gradient(0deg,rgba(255,255,255,.12) 0 1px,rgba(0,0,0,.04) 1px 3px),linear-gradient(180deg,var(--silver-1),var(--silver-2) 55%,var(--silver-3))}
  .finish-gold{background:linear-gradient(135deg,var(--gold-1) 0%,var(--gold-2) 45%,#f3d884 70%,var(--gold-3) 100%)}

  /* front elements */
  .casino-mark{position:absolute;left:110px;top:10px;width:160px;text-align:center}
  .casino-mark .dot{display:block;width:30px;height:30px;border-radius:50%;margin:0 auto 6px;background:linear-gradient(180deg,#d0d0d0,#777)}
  .casino-mark .name{font-family:"Cinzel",serif;font-size:15px;font-weight:600;letter-spacing:1px;line-height:1.15}
  .finish-black .casino-mark .name{color:var(--white)}
  .finish-silver .casino-mark .name,.finish-gold .casino-mark .name{color:var(--navy)}

  .group-mark{position:absolute;right:10px;top:10px;width:72px;text-align:center}
  .group-mark .square{display:block;width:40px;height:40px;margin:0 auto 6px;background:linear-gradient(135deg,#e0307a,#f2a02c 50%,#2fa8e0)}
  .group-mark .name{font-family:"Cinzel",serif;font-size:10px;font-weight:600;letter-spacing:1px;line-height:1.15}
  .finish-black .group-mark .name{color:var(--white)}
  .finish-silver .group-mark .name,.finish-gold .group-mark .name{color:#333}

  .chip{position:absolute;left:36px;top:76px;width:64px;height:58px;background:var(--white);border:1px solid #999;border-radius:3px}

  .tier-band{position:absolute;left:0;right:0;top:114px;height:28px;display:flex;align-items:center;justify-content:flex-end;padding-right:38px;font-family:"Cinzel",serif}
  .tier-band .tier{font-size:22px;font-weight:700}
  .tier-band .tier small{font-size:11px;font-weight:600;margin-left:4px}
  .tier-limited{background:linear-gradient(180deg,#1a1a1a,#000);justify-content:center;padding-left:90px;padding-right:0}
  .tier-limited .tier{font-size:16px;color:var(--gold-text);letter-spacing:1px}
  .tier-limited .tier small{font-size:8px}
  .tier-platinum{background:linear-gradient(180deg,#1b1b1b,#000);justify-content:center;padding-left:70px;padding-right:0}
  .tier-platinum .tier{color:var(--white)}
  .tier-gold{background:linear-gradient(180deg,#e9c25c,var(--gold-3));justify-content:center;padding-left:70px;padding-right:0}
  .tier-gold .tier{color:var(--ink)}

  .valid{position:absolute;left:0;right:0;font-family:"Cinzel",serif;font-size:12px;text-align:center;letter-spacing:.3px}
  .holder{position:absolute;left:0;right:0;bottom:0;font-family:"Cinzel",serif;font-size:16px;font-weight:600;text-align:center;letter-spacing:.5px}

  .row-1.front .valid{top:160px;color:var(--gold-text)}
  .row-1.front .rule{position:absolute;left:0;right:0;top:192px;height:1px;background:var(--gold-2)}
  .row-1.front .holder{height:46px;line-height:46px;background:#0a0a0a;color:var(--gold-text)}

  .row-2.front .valid{top:162px;color:var(--ink)}
  .row-2.front .holder{height:46px;line-height:46px;background:linear-gradient(180deg,#1c1c1c,#000);color:var(--white)}

  .row-3.front .dark-band{position:absolute;left:0;right:0;top:145px;height:48px;background:linear-gradient(180deg,#1b1b1b,#000)}
  .row-3.front .valid{top:161px;color:var(--white)}
  .row-3.front .holder{height:46px;line-height:46px;color:var(--ink)}

  /* back elements */
  .back-head{position:absolute;left:0;right:0;top:0;height:30px;display:flex;align-items:center;justify-content:center;font-family:"Cinzel",serif;font-size:13px;font-weight:700;letter-spacing:.3px}
  .back-head .warn{position:absolute;right:10px;top:4px;width:24px;height:22px}
  .finish-black .back-head{color:var(--gold-text);background:linear-gradient(180deg,#2c2c2c,#1a1a1a)}
  .finish-silver .back-head,.finish-gold .back-head{top:8px;height:22px;color:var(--ink);background:linear-gradient(180deg,#fff,#e8e8e8)}
  .finish-gold.back .back-head{background:linear-gradient(180deg,#fff,#f4efe2)}

  .terms{position:absolute;left:8px;right:8px;top:34px;list-style:none;font-size:7.3px;line-height:1.25;text-align:justify}
  .finish-silver .terms,.finish-gold .terms{top:36px}
  .terms li::before{content:"• "}
  .finish-black .terms{color:var(--white)}
  .finish-silver .terms,.finish-gold .terms{color:var(--ink)}

  .gold-sweep{position:absolute;left:0;right:0;top:140px;height:90px;background:radial-gradient(ellipse at 70% 100%,rgba(255,246,205,.7),rgba(255,246,205,0) 60%)}

  .contact{position:absolute;left:6px;right:6px;bottom:4px;height:18px;border-top:2px solid;display:flex;align-items:center;justify-content:space-between;font-size:6px;font-weight:600;padding:0 2px}
  .contact .pair{display:flex;gap:14px}
  .finish-black .contact{color:var(--white);border-color:var(--white)}
  .finish-silver .contact,.finish-gold .contact{color:var(--ink);border-color:var(--ink)}
</style>
</head>
<body>

<!-- Vireo Card Limited -->
<section class="card front finish-black row-1">
  <div class="casino-mark"><span class="dot"></span><span class="name">Mirabel Hotel &amp; Casino</span></div>
  <div class="group-mark"><span class="square"></span><span class="name">Torvel Global</span></div>
  <div class="chip"></div>
  <div class="tier-band tier-limited"><span class="tier">Vireo Card Limited<small>( Grandest)</small></span></div>
  <p class="valid">VALID IN ALL TORVEL GLOBAL CASINOS</p>
  <div class="rule"></div>
  <p class="holder">OWEN MARLOW ID: 123456</p>
</section>
<section class="card back finish-black row-1">
  <h2 class="back-head">Valid in all TORVEL GLOBAL Casinos
    <svg class="warn" viewBox="0 0 24 22"><path d="M12 1 23 21H1Z" fill="#fff"/><rect x="11" y="7" width="2" height="8" fill="#111"/><rect x="11" y="16.5" width="2" height="2" fill="#111"/></svg>
  </h2>
  <ul class="terms">
    <li>This card is property of Torvel Global</li>
    <li>This card is not transferable and may not be used by any person other than the named card holder</li>
    <li>Lost, stolen or damaged cards are to be notified immediately to any Torvel Global Casino</li>
    <li>Membership privileges are available only on the presentation of your current membership card together with photographic identification and proof of entitlement to any concession benefits</li>
    <li>Management reserve the right to update or change the terms and conditions without prior notice and management decision is final</li>
    <li>Use of this card constitutes acceptance of the terms and conditions</li>
  </ul>
  <footer class="contact"><span class="pair"><span>[P]: +31 20 555 0148</span><span>[W]: www.torvelglobal.example</span></span><span>Lindenhof 18, Havenstad 3001, Nederland</span></footer>
</section>

<!-- Platinum -->
<section class="card front finish-silver row-2">
  <div class="casino-mark"><span class="dot"></span><span class="name">Mirabel Hotel &amp; Casino</span></div>
  <div class="group-mark"><span class="square"></span><span class="name">Torvel Global</span></div>
  <div class="chip"></div>
  <div class="tier-band tier-platinum"><span class="tier">Platinum<small>(Grander)</small></span></div>
  <p class="valid">VALID IN ALL TORVEL GLOBAL CASINOS</p>
  <p class="holder">OWEN MARLOW ID: 123456</p>
</section>
<section class="card back finish-silver row-2">
  <h2 class="back-head">Valid in all TORVEL GLOBAL Casinos
    <svg class="warn" viewBox="0 0 24 22"><path d="M12 1 23 21H1Z" fill="#fff" stroke="#111" stroke-width="1.5"/><rect x="11" y="7" width="2" height="8" fill="#111"/><rect x="11" y="16.5" width="2" height="2" fill="#111"/></svg>
  </h2>
  <ul class="terms">
    <li>This card is property of Torvel Global</li>
    <li>This card is not transferable and may not be used by any person other than the named card holder</li>
    <li>Lost, stolen or damaged cards are to be notified immediately to any Torvel Global Casino</li>
    <li>Membership privileges are available only on the presentation of your current membership card together with photographic identification and proof of entitlement to any concession benefits</li>
    <li>Management reserve the right to update or change the terms and conditions without prior notice and management decision is final</li>
    <li>Use of this card constitutes acceptance of the terms and conditions</li>
  </ul>
  <footer class="contact"><span class="pair"><span>[P]: +31 20 555 0148</span><span>[W]: www.torvelglobal.example</span></span><span>Lindenhof 18, Havenstad 3001, Nederland</span></footer>
</section>

<!-- Gold -->
<section class="card front finish-gold row-3">
  <div class="casino-mark"><span class="dot"></span><span class="name">Mirabel Hotel &amp; Casino</span></div>
  <div class="group-mark"><span class="square"></span><span class="name">Torvel Global</span></div>
  <div class="chip"></div>
  <div class="tier-band tier-gold"><span class="tier">Gold<small>(Normal)</small></span></div>
  <div class="dark-band"></div>
  <p class="valid">VALID IN ALL TORVEL GLOBAL CASINOS</p>
  <p class="holder">OWEN MARLOW ID: 123456</p>
</section>
<section class="card back finish-gold row-3">
  <div class="gold-sweep" role="img" aria-label="Soft light wave across the gold background"></div>
  <h2 class="back-head">Valid in all TORVEL GLOBAL Casinos
    <svg class="warn" viewBox="0 0 24 22"><path d="M12 1 23 21H1Z" fill="#fff" stroke="#111" stroke-width="1.5"/><rect x="11" y="7" width="2" height="8" fill="#111"/><rect x="11" y="16.5" width="2" height="2" fill="#111"/></svg>
  </h2>
  <ul class="terms">
    <li>This card is property of Torvel Global</li>
    <li>This card is not transferable and may not be used by any person other than the named card holder</li>
    <li>Lost, stolen or damaged cards are to be notified immediately to any Torvel Global Casino</li>
    <li>Membership privileges are available only on the presentation of your current membership card together with photographic identification and proof of entitlement to any concession benefits</li>
    <li>Management reserve the right to update or change the terms and conditions without prior notice and management decision is final</li>
    <li>Use of this card constitutes acceptance of the terms and conditions</li>
  </ul>
  <footer class="contact"><span class="pair"><span>[P]: +31 20 555 0148</span><span>[W]: www.torvelglobal.example</span></span><span>Lindenhof 18, Havenstad 3001, Nederland</span></footer>
</section>

</body>
</html>
```